Design for web app with Plinkora Stratum Craft - Tarvo7 SMS consult

We are developing a web app that will work in browsers. Its main purpose is to allow for users (signing up and logging in with their phone number) to track their habbits and select consultants to whom they can send SMS for help.

The wireframes of the app can be accessed here (pdf):
https://files.plinkora.example/d/7K2mWqLzXv4NtRb9HcJpYsAeUfDg3/view

NB!: Please do not follow the mockups 100% literally, but the Plinkora Stratum craft guidelines.

The technical specifications and descriptions of the web app's functionalities are available in the link below:
https://papers.plinkora.example/doc/4HsTnV8bQeZr2LmXwYcKpDjAuFgN6oRiE5tW1yMx/edit

Requirements for the design:

- The design should be provided as PSD, where each page/section should be in its own PSD file OR all pages/sections should be represented as folder groups in a single PSD file.

- All graphical elements in the design should be delivered as single layers which can then be extracted from the PSD.

- All graphical elements (icons, graphical buttons, etc.) should be provided as vector objects in the PSD, so that they can be exported into different sizes without loss of quality (for responsiveness).

- The design should use either web safe fonts or Plinkora Type.

Instructions for the design:
The design should be based on Plinkora Stratum Craft - http://www.plinkora.example/craft/spec/stratum-craft/overview.html

Please also provide an app icon and suggest a logo for the app.

Requirements
Must have
• Based on Plinkora Stratum Craft
• Flat
Nice to have
• Nice looking and not so stiff as the default Plinkora Stratum Craft, but it is important to follow their guidelines.
Should not have
• 3D

```html
<!DOCTYPE html>
<html lang="en">
<head>
<meta charset="utf-8">
<title>Tarvo7 – Consultant</title>
<link rel="stylesheet" href="https://fonts.googleapis.com/css2?family=Montserrat:wght@400;700&family=Open+Sans:wght@300;400&display=swap">
<style>
  :root {
    --bar-blue: #0172a8;
    --body-bg: #252934;
    --green: #548840;
    --red: #ff6464;
    --steel-blue: #3a80a8;
    --rule: #363b47;
    --name-grey: #9a9da5;
    --role-grey: #6e727c;
    --quote-grey: #b3b6bd;
    --placeholder: #6b6f79;
    --white: #ffffff;
  }
  * { box-sizing: border-box; margin: 0; padding: 0; }
  html, body { width: 676px; height: 1200px; overflow: hidden; }
  body { background: var(--body-bg); font-family: "Open Sans", sans-serif; position: relative; }

  .app-bar { position: absolute; left: 0; top: 0; width: 676px; height: 147px; background: var(--bar-blue); color: var(--white); }
  .status-bar { position: absolute; left: 0; top: 0; width: 100%; height: 42px; font-family: "Open Sans", sans-serif; font-size: 22px; }
  .status-left { position: absolute; left: 6px; top: 6px; display: flex; align-items: center; gap: 6px; }
  .status-time { position: absolute; left: 0; right: 0; top: 5px; text-align: center; font-weight: 400; }
  .status-right { position: absolute; right: 8px; top: 6px; display: flex; align-items: center; gap: 8px; }
  .title { position: absolute; left: 0; right: 0; top: 78px; text-align: center; font-size: 32px; font-weight: 400; letter-spacing: 0.5px; }
  .back-btn { position: absolute; left: 36px; top: 86px; }
  .menu-btn { position: absolute; left: 606px; top: 91px; }

  .profile { position: absolute; left: 42px; top: 193px; display: flex; align-items: center; }
  .avatar { width: 104px; height: 104px; border-radius: 50%; background: radial-gradient(circle at 50% 40%, #e7c58f 0%, #c99a63 45%, #8b6a4e 100%); }
  .profile-text { margin-left: 28px; margin-top: -6px; }
  .profile-name { font-family: "Open Sans", sans-serif; font-weight: 400; font-size: 33px; color: var(--name-grey); }
  .profile-role { font-family: "Montserrat", sans-serif; font-size: 21px; color: var(--role-grey); margin-top: 2px; }

  .btn { position: absolute; display: flex; align-items: center; justify-content: center; border-radius: 3px; font-family: "Montserrat", sans-serif; font-weight: 700; color: var(--white); font-size: 32px; }
  .btn-call { left: 63px; top: 333px; width: 555px; height: 105px; background: var(--green); }

  .rule { position: absolute; left: 34px; width: 608px; height: 1px; background: var(--rule); }
  .quote { position: absolute; left: 40px; width: 596px; top: 506px; text-align: center; font-size: 28px; line-height: 44px; color: var(--quote-grey); }

  .vote { position: absolute; left: 60px; top: 673px; width: 555px; height: 105px; display: flex; border-radius: 3px; overflow: hidden; }
  .vote-up { flex: 0 0 277px; background: var(--green); display: flex; align-items: center; justify-content: center; }
  .vote-down { flex: 1; background: var(--red); display: flex; align-items: center; justify-content: center; }

  .notes { position: absolute; left: 34px; top: 834px; width: 611px; height: 159px; border: 1px solid var(--rule); padding: 16px 18px; font-family: "Montserrat", sans-serif; font-size: 21px; color: var(--placeholder); }

  .btn-stats { left: 34px; top: 1051px; width: 287px; height: 106px; background: var(--steel-blue); justify-content: flex-start; padding-left: 26px; gap: 30px; }
  .btn-gem { left: 355px; top: 1051px; width: 287px; height: 106px; background: var(--green); }
</style>
</head>
<body>
  <header class="app-bar">
    <div class="status-bar">
      <div class="status-left">
        <svg width="70" height="14" viewBox="0 0 70 14" aria-hidden="true">
          <circle cx="7" cy="7" r="6" fill="#fff"/><circle cx="21" cy="7" r="6" fill="#fff"/><circle cx="35" cy="7" r="6" fill="#fff"/>
          <circle cx="49" cy="7" r="5.4" fill="none" stroke="#fff" stroke-width="1.2"/><circle cx="63" cy="7" r="5.4" fill="none" stroke="#fff" stroke-width="1.2"/>
        </svg>
        <span>VELTO</span>
        <svg width="26" height="20" viewBox="0 0 26 20" aria-hidden="true">
          <path d="M1 7 A17 17 0 0 1 25 7 L13 19 Z" fill="#fff"/>
        </svg>
      </div>
      <div class="status-time">4:21 PM</div>
      <div class="status-right">
        <svg width="14" height="24" viewBox="0 0 14 24" aria-hidden="true"><path d="M1 6 L12 17 L7 22 L7 2 L12 7 L1 18" fill="none" stroke="#8fc1dc" stroke-width="1.8"/></svg>
        <span>100%</span>
        <svg width="50" height="22" viewBox="0 0 50 22" aria-hidden="true">
          <rect x="1" y="1" width="44" height="20" rx="4" fill="none" stroke="#fff" stroke-width="1.5"/>
          <rect x="3.5" y="3.5" width="39" height="15" rx="2" fill="#fff"/>
          <rect x="46.5" y="7" width="3" height="8" rx="1" fill="#fff"/>
        </svg>
      </div>
    </div>
    <svg class="back-btn" width="16" height="26" viewBox="0 0 16 26" aria-label="Back"><path d="M13 2 L3 13 L13 24" fill="none" stroke="#fff" stroke-width="3.4" stroke-linecap="round" stroke-linejoin="round"/></svg>
    <h1 class="title">02.04.2015</h1>
    <svg class="menu-btn" width="33" height="16" viewBox="0 0 33 16" aria-label="Menu"><g stroke="#fff" stroke-width="2.2"><line x1="0" y1="1.5" x2="33" y2="1.5"/><line x1="0" y1="8" x2="33" y2="8"/><line x1="0" y1="14.5" x2="33" y2="14.5"/></g></svg>
  </header>

  <section class="profile">
    <div class="avatar" role="img" aria-label="Consultant portrait photo"></div>
    <div class="profile-text">
      <div class="profile-name">Marin Dovesk</div>
      <div class="profile-role">Specialst on Nutrition</div>
    </div>
  </section>

  <div class="btn btn-call">CALL ME</div>

  <div class="rule" style="top:484px"></div>
  <p class="quote">“I can help you to improve your healt situation”</p>
  <div class="rule" style="top:621px"></div>

  <div class="vote">
    <div class="vote-up" aria-label="Like">
      <svg width="58" height="50" viewBox="0 0 58 50" aria-hidden="true">
        <rect x="1" y="20" width="14" height="27" fill="#c6dcbc"/>
        <path d="M18 21 L29 8 L31 1 C36 1 38 6 36 13 L34 19 L51 19 C56 19 57 24 54 27 C57 30 56 34 52 35 C55 38 53 42 49 42 C51 45 49 48 45 48 L24 48 L18 45 Z" fill="none" stroke="#c6dcbc" stroke-width="2.4" stroke-linejoin="round"/>
      </svg>
    </div>
    <div class="vote-down" aria-label="Dislike">
      <svg width="58" height="50" viewBox="0 0 58 50" aria-hidden="true">
        <rect x="43" y="3" width="14" height="27" fill="#ffd4d4"/>
        <path d="M40 29 L29 42 L27 49 C22 49 20 44 22 37 L24 31 L7 31 C2 31 1 26 4 23 C1 20 2 16 6 15 C3 12 5 8 9 8 C7 5 9 2 13 2 L34 2 L40 5 Z" fill="none" stroke="#ffd4d4" stroke-width="2.4" stroke-linejoin="round"/>
      </svg>
    </div>
  </div>

  <div class="notes">Notes...</div>

  <div class="btn btn-stats">
    <svg width="48" height="48" viewBox="0 0 48 48" aria-hidden="true">
      <g stroke="#a9cbe0" stroke-width="1.6" fill="none">
        <line x1="2" y1="0" x2="2" y2="46" stroke-dasharray="2 3"/>
        <line x1="2" y1="46" x2="48" y2="46" stroke-dasharray="2 3"/>
        <polyline points="2,44 10,34 22,28 32,18 46,2"/>
        <circle cx="10" cy="34" r="3" fill="#3a80a8"/><circle cx="22" cy="28" r="3" fill="#3a80a8"/><circle cx="32" cy="18" r="3" fill="#3a80a8"/>
      </g>
    </svg>
    <span>STATITCS</span>
  </div>
  <div class="btn btn-gem">GEM</div>
</body>
</html>
```